This is a Pet Servce company and I need a webpage for it.

A web page that show my flexible services that are available along fair pricing. The files uploaded are my logo and a couple seals or symbols that could go on the bottom or somewhere else.
The page should show a friendly excitement. I really do want to help the community and provide a taxi service and helpful for elderly owners, as well as, clients who have busy and unpredictable schedules and emergencies. Reliability is key to our service and we take pride in it.
I have experience with small caged animals such as rabbits, chickens, and of course horses and donkeys, the dogs and cats! My services will give piece of mind whether a planned or unpredictable situation!
The colors I am favoring are: spring green, and maybe scarlet lettering or white.
The final design wants to portray a sophisticated and professional look.
I want clients to know it is our goal to provide excellent services for the love of the animal.
Somewhere on the page I would like to have these words written, "For the Love and Care of Your Pets".

Target Market(s)

Pet Owners, Pet Lovers

Industry/Entity Type

Pet

Number of Pages Required

1 page

Font styles to use
Decorative

Colors
9ccb3b
85cae6
ec1f27
cadf82

Requirements
Must have
• The page needs to convey what is said in my description, "I really do want to help the community and provide a taxi service and helpful for elderly owners, as well as, clients who have busy and unpredictable schedules and emergencies. Reliability is key to our service and we take pride in it." The page should also mention my experience and include the logo mentioned and provided, as well as, the two associations seals for which I belong to.
Nice to have
• curious about scarlet lettering in monotype corosiva font with a springy green background. The green could be grass..no cartoony stuff or pictures please. Photos of animals are nice. So are clouds and trees
Should not have
• cartoony looking characters or words or pictures, of animals or humans. Please do not add hyperlinks for others to follow, such as, "Services" like there would be for a site. This is a webpage, instead. I will need a site later as the business grows.

```html
<!DOCTYPE html>
<html lang="en">
<head>
<meta charset="utf-8">
<title>Paw Haven — For the Love and Care of Your Animals</title>
<link href="https://fonts.googleapis.com/css2?family=Open+Sans:wght@300;400;600;700&family=Oswald:wght@500;700&display=swap" rel="stylesheet">
<style>
:root{
  --green:#9ccb3b;
  --green-soft:#cadf82;
  --sky:#85cae6;
  --scarlet:#ec1f27;
  --dark:#1c1c1c;
  --footer:#1e1e1e;
  --ink:#333;
  --white:#fff;
}
*{box-sizing:border-box;margin:0;padding:0}
html,body{width:1200px;height:3237px;overflow:hidden}
body{font-family:"Open Sans",sans-serif;color:var(--ink);background:var(--white);position:relative}

/* hero */
.hero{position:absolute;left:0;top:0;width:1200px;height:641px;overflow:hidden}
.hero-photo{position:absolute;inset:0;background:linear-gradient(160deg,#dcebf3 0%,#e4edd2 22%,#cfe09f 40%,#e0b48c 56%,#c98a5a 66%,#d9c2a6 76%,#a9c868 88%,#7fab3f 100%)}
.topbar{position:absolute;top:65px;left:0;width:1200px;height:65px;background:var(--green)}
.brand{position:absolute;left:0;top:0;width:324px;height:65px;background:var(--white);border-right:5px solid var(--scarlet);display:flex;align-items:center;padding-left:74px;gap:12px}
.brand-dot{width:30px;height:30px;background:#111;border-radius:50%}
.brand-name{font-family:"Oswald",sans-serif;font-weight:700;font-size:24px;color:#111}
.follow{position:absolute;left:624px;top:18px;font-size:15px;color:#2d3b10;display:flex;align-items:center;gap:6px}
.follow span{width:28px;height:28px;background:#111;border-radius:50%;display:inline-block}
.follow em{font-style:normal;margin-right:6px}
.search{position:absolute;left:948px;top:18px;width:200px;height:28px;background:var(--white)}
.search svg{position:absolute;right:6px;top:5px}
.hero-title{position:absolute;left:58px;top:298px;font-family:"Oswald",sans-serif;font-weight:700;font-size:45px;color:var(--scarlet);letter-spacing:.5px}
.hero-title b{color:#161616;font-weight:700}
.hero-sub{position:absolute;left:58px;top:368px;font-size:36px;font-weight:300;color:#222}

/* services */
.services{position:absolute;left:0;top:641px;width:1200px;height:546px;background:var(--dark);border-top:5px solid #555}
.sec-head{position:absolute;left:0;width:1200px;display:flex;align-items:center;justify-content:center;gap:22px}
.sec-head .line{height:2px;background:#fff;width:250px;position:relative}
.sec-head .line::after{content:"";position:absolute;top:-5px;width:12px;height:12px;border-radius:50%;background:#fff}
.sec-head .line.l::after{right:-6px}
.sec-head .line.r::after{left:-6px}
.services h2{font-family:"Oswald",sans-serif;font-weight:500;font-size:34px;color:var(--green)}
.services .lead{position:absolute;top:88px;width:1200px;text-align:center;color:#eee;font-size:16px}
.service{position:absolute;width:270px;text-align:center;color:#fff;font-size:28px;font-weight:300}
.service .pic{width:216px;height:216px;border-radius:50%;border:5px solid #fff;margin:0 auto 20px}
.service.active{border:1px solid #444;border-radius:4px;background:#222}
.pic.dog{background:linear-gradient(180deg,#e7e2d6 0%,#c99b62 40%,#8a5d34 60%,#b9b2a4 80%,#6d6a62 100%)}
.pic.cat{background:linear-gradient(135deg,#c4602f 0%,#e08a54 35%,#e8e2d6 55%,#7a8a60 80%,#3f5a34 100%)}
.pic.critter{background:radial-gradient(circle at 50% 40%,#eef6d2,#b8dc6a 55%,#7eb236 100%);display:flex;align-items:center;justify-content:center;gap:12px}
.pic.critter i{width:42px;height:42px;border:2px solid #1c2a08;display:flex;align-items:center;justify-content:center}
.pic.taxi{background:linear-gradient(160deg,#f6d12a 0%,#e9b80f 40%,#8a8a86 65%,#4c4c4c 100%)}

/* welcome */
.welcome{position:absolute;left:0;top:1187px;width:1200px;height:403px;background:var(--white)}
.welcome .sec-head .line{background:#333;width:240px}
.welcome .sec-head .line::after{background:#111}
.welcome h2{font-family:"Oswald",sans-serif;font-weight:700;font-size:40px;color:var(--scarlet)}
.welcome .tag{position:absolute;top:135px;width:1200px;text-align:center;font-size:17px;color:#555}
.welcome .body{position:absolute;left:88px;top:195px;width:1024px;text-align:center;font-size:13px;line-height:27px;color:#666}
.welcome .more{position:absolute;top:320px;width:1200px;text-align:center;font-size:13px;color:var(--scarlet)}

/* gallery */
.gallery{position:absolute;left:0;top:1590px;width:1200px;height:665px;background:linear-gradient(180deg,#c4e07e 0%,#a9d257 22%,#8cbf3f 55%,#7cb234 80%,#93c44a 100%)}
.gallery .sec-head .line{width:360px;background:#fff}
.gallery h2{font-family:"Oswald",sans-serif;font-weight:700;font-size:40px;color:#1c1c1c}
.tile{position:absolute}
.t1{left:60px;top:214px;width:177px;height:153px;background:linear-gradient(160deg,#e9e6df 0%,#c49460 45%,#7d5632 65%,#9a968c 100%)}
.t2{left:60px;top:391px;width:177px;height:153px;background:linear-gradient(160deg,#7fa84a 0%,#d9b874 45%,#e7c98a 60%,#7ea348 100%)}
.t3{left:257px;top:214px;width:341px;height:330px;background:linear-gradient(180deg,#de3b35,#c93230);display:flex;align-items:center;justify-content:center}
.t3 span{width:58px;height:58px;border-radius:50%;background:rgba(255,255,255,.85);display:flex;align-items:center;justify-content:center}
.t4{left:615px;top:214px;width:328px;height:330px;background:linear-gradient(145deg,#2b2b2b 0%,#ececec 30%,#d99a5a 55%,#b87a44 75%,#ededed 100%)}
.t5{left:962px;top:214px;width:175px;height:153px;background:linear-gradient(160deg,#f6d12a 0%,#e8b80e 45%,#8d8d89 70%,#555 100%)}
.t6{left:962px;top:391px;width:175px;height:153px;background:linear-gradient(180deg,#2f5d22 0%,#5e8f35 40%,#f2f2f2 60%,#8cbc4e 100%)}

/* offers */
.card{position:absolute;top:2320px;height:464px;background:linear-gradient(180deg,#fff,#f1f1f1);border:1px solid #ddd;border-radius:3px}
.discounts{left:58px;width:520px}
.available{left:600px;width:541px}
.discounts h3{position:absolute;left:24px;top:14px;width:470px;font-size:38px;font-weight:400;color:#222}
.discounts h3 strong{display:block;font-family:"Oswald",sans-serif;font-weight:700;color:var(--scarlet);text-align:right;font-size:40px}
.discounts .signup{position:absolute;left:24px;top:152px;font-size:24px;color:var(--green);font-weight:600}
.discounts ul{position:absolute;left:30px;top:197px;width:350px;list-style:none;font-size:17px;line-height:22px;color:#555}
.discounts li{margin-bottom:13px;padding-left:16px;position:relative}
.discounts li::before{content:"";position:absolute;left:0;top:7px;border-left:6px solid var(--scarlet);border-top:4px solid transparent;border-bottom:4px solid transparent}
.signup-bar{position:absolute;left:30px;top:342px;width:452px;height:78px;background:var(--green);display:flex;align-items:center;padding:0 14px}
.signup-bar b{font-size:18px;font-weight:400;color:#1c2a08;line-height:20px;width:98px}
.signup-bar .field{width:236px;height:38px;background:#fff;font-size:13px;color:#999;padding:11px 10px}
.signup-bar .btn{width:84px;height:38px;background:var(--scarlet);color:#fff;font-size:16px;font-weight:600;text-align:center;line-height:38px}
.available h3{position:absolute;left:24px;top:18px;font-family:"Oswald",sans-serif;font-weight:700;font-size:48px;color:#222}
.available .need{position:absolute;left:24px;top:96px;font-size:28px;color:var(--scarlet)}
.available .intro{position:absolute;left:24px;top:140px;width:470px;font-size:16px;line-height:22px;color:#444}
.available .intro b{display:block;color:#222}
.feature{position:absolute;top:252px;width:150px;text-align:center;font-size:14px;font-weight:700;line-height:18px;color:#222}
.feature .ic{width:94px;height:94px;border-radius:50%;margin:0 auto 14px;display:flex;align-items:center;justify-content:center}
.f1{left:24px}.f1 .ic{background:var(--scarlet)}
.f2{left:190px}.f2 .ic{background:var(--green)}
.f3{left:361px}.f3 .ic{background:var(--green)}

/* footer */
.site-footer{position:absolute;left:0;top:2851px;width:1200px;height:343px;background:var(--footer);color:#bbb}
.col{position:absolute;top:40px}
.col h4{font-size:21px;font-weight:400;color:#fff;padding-bottom:18px;border-bottom:1px solid #333;margin-bottom:20px}
.c1{left:58px;width:230px}.c2{left:330px;width:270px}.c3{left:641px;width:235px}.c4{left:919px;width:230px}
.c1 p{font-size:12px;line-height:24px}
.badges{display:flex;gap:30px;align-items:center;margin-top:20px}
.badge-round{width:100px;height:100px;border-radius:50%;background:#e4e4e4}
.badge-square{width:60px;height:60px;background:#e4e4e4}
.input{height:36px;border:1px solid #333;font-size:11px;color:#999;padding:10px 12px;margin-bottom:10px}
.input.msg{height:60px}
.send{width:160px;height:32px;background:#333;color:#ddd;font-size:11px;letter-spacing:1px;text-align:center;line-height:32px;font-weight:600}
.c4 p{font-size:12px;line-height:24px}
.social{display:flex;gap:14px;margin-top:16px;align-items:center}
.social span{width:22px;height:22px;background:#ddd;display:block}
.social span:first-child{width:36px;height:36px;background:#2a9fd8}
.copyright{position:absolute;left:0;top:3194px;width:1200px;height:43px;background:var(--scarlet);color:#fff;font-size:14px;text-align:center;line-height:43px}
</style>
</head>
<body>

<header class="hero">
  <div class="hero-photo" role="img" aria-label="Bright photo of a smiling young woman hugging a happy beagle in a sunny spring meadow"></div>
  <div class="topbar">
    <div class="brand"><span class="brand-dot"></span><span class="brand-name">Paw Haven</span></div>
    <div class="follow"><em>Follow Us on:</em><span></span><span></span><span></span><span></span><span></span></div>
    <div class="search"><svg width="18" height="18" viewBox="0 0 18 18"><circle cx="7" cy="7" r="5.5" fill="none" stroke="#111" stroke-width="2"/><line x1="11" y1="11" x2="16.5" y2="16.5" stroke="#111" stroke-width="2.4"/></svg></div>
  </div>
  <h1 class="hero-title">FOR THE <b>LOVE &amp;</b> CARE</h1>
  <p class="hero-sub">of Your Animals</p>
</header>

<section class="services">
  <div class="sec-head" style="top:30px"><span class="line l"></span><h2>Pet Services</h2><span class="line r"></span></div>
  <p class="lead">Proactively ipsum media appropriately materials without lorem networks that native cultivate it daycare</p>
  <div class="service" style="left:44px;top:196px"><div class="pic dog" role="img" aria-label="Photo of a boxer dog on a leash walk"></div>Dog Walking</div>
  <div class="service" style="left:325px;top:196px"><div class="pic cat" role="img" aria-label="Photo of a cat being held"></div>Cat Care</div>
  <div class="service active" style="left:609px;top:162px;width:269px;height:341px;padding-top:33px"><div class="pic critter" role="img" aria-label="Photo of a small rabbit in green grass"><i><svg width="18" height="18" viewBox="0 0 18 18"><circle cx="7" cy="7" r="5" fill="none" stroke="#1c2a08" stroke-width="2"/><line x1="11" y1="11" x2="16" y2="16" stroke="#1c2a08" stroke-width="2.4"/></svg></i><i><svg width="18" height="18" viewBox="0 0 18 18"><rect x="2" y="7" width="8" height="4" rx="2" transform="rotate(-45 6 9)" fill="none" stroke="#1c2a08" stroke-width="2"/><rect x="8" y="7" width="8" height="4" rx="2" transform="rotate(-45 12 9)" fill="none" stroke="#1c2a08" stroke-width="2"/></svg></i></div>Critter Care</div>
  <div class="service" style="left:894px;top:196px"><div class="pic taxi" role="img" aria-label="Photo of a dog stepping out of a yellow taxi"></div>Pet Taxi</div>
</section>

<section class="welcome">
  <div class="sec-head" style="top:68px"><span class="line l"></span><h2>WELCOME TO PAW HAVEN</h2><span class="line r"></span></div>
  <p class="tag">For the Love and Care of Your Animals</p>
  <p class="body">simply dummy text of the printing and typesetting industry. Lorem Ipsum has been the industry's standard dummy text ever since the 1500s, when an unknown printer took a galley of type and scrambled it to make a type specimen book. It has survived not only five centuries, but also the leap into electronic typesetting, remaining essentially unchanged. It was popularised in the 1960s with the release of TypeSheet sheets containing Lorem Ipsum passages, and more recently with desktop publishing software like PageForge including versions of Lorem Ipsum.</p>
  <p class="more">Read More &rarr;</p>
</section>

<section class="gallery" role="img" aria-label="Soft blurred green lawn, trees and a house behind the gallery">
  <div class="sec-head" style="top:62px"><span class="line l"></span><h2>PET GALLERY</h2><span class="line r"></span></div>
  <div class="tile t1" role="img" aria-label="Photo of a boxer dog walking"></div>
  <div class="tile t2" role="img" aria-label="Photo of puppies and kittens on grass"></div>
  <div class="tile t3" role="img" aria-label="Photo of a hen under a red overlay"><span><svg width="26" height="26" viewBox="0 0 26 26"><circle cx="11" cy="11" r="7" fill="none" stroke="#d93a35" stroke-width="2.4"/><line x1="16" y1="16" x2="23" y2="23" stroke="#d93a35" stroke-width="3"/><line x1="8" y1="11" x2="14" y2="11" stroke="#d93a35" stroke-width="2"/><line x1="11" y1="8" x2="11" y2="14" stroke="#d93a35" stroke-width="2"/></svg></span></div>
  <div class="tile t4" role="img" aria-label="Photo of two cats lying together"></div>
  <div class="tile t5" role="img" aria-label="Photo of a dog leaving a yellow taxi"></div>
  <div class="tile t6" role="img" aria-label="Photo of a white rabbit on grass"></div>
</section>

<div class="card discounts">
  <h3>Discounts Available for <strong>ESTABLISHED CLIENTS</strong></h3>
  <p class="signup">Sign up for:</p>
  <ul>
    <li>Discount Information</li>
    <li>Our Free Newsletter</li>
    <li>Exclusive discounts for senior citizens age 50+</li>
  </ul>
  <div class="signup-bar"><b>SIGN UP<br>TODAY!</b><div class="field">Email Address</div><div class="btn">Submit</div></div>
</div>

<div class="card available">
  <h3>ALWAYS AVAILABLE</h3>
  <p class="need">for Emergent Needs</p>
  <p class="intro"><b>Paw Haven provide you All 24 hours availability.</b>simply dummy text of the printing and typesetting industry. Lorem Ipsum has been the industry's.</p>
  <div class="feature f1"><div class="ic"><svg width="50" height="50" viewBox="0 0 50 50"><path d="M10 30 A16 16 0 1 1 40 30" fill="none" stroke="#fff" stroke-width="3"/><polyline points="36,26 40,31 44,26" fill="none" stroke="#fff" stroke-width="3"/><text x="25" y="30" font-family="Open Sans,sans-serif" font-size="12" font-weight="700" fill="#fff" text-anchor="middle">24</text></svg></div>24/7 EMERGENCY AVAILABLE</div>
  <div class="feature f2"><div class="ic"><svg width="50" height="50" viewBox="0 0 50 50"><line x1="12" y1="12" x2="38" y2="38" stroke="#fff" stroke-width="5" stroke-linecap="round"/><line x1="38" y1="12" x2="12" y2="38" stroke="#fff" stroke-width="5" stroke-linecap="round"/></svg></div>EXPERT &amp; PROFESSIONAL</div>
  <div class="feature f3"><div class="ic"><svg width="50" height="50" viewBox="0 0 50 50"><circle cx="25" cy="20" r="11" fill="none" stroke="#fff" stroke-width="3"/><polyline points="18,29 15,44 25,39 35,44 32,29" fill="none" stroke="#fff" stroke-width="3"/></svg></div>SATISFACTION GUARANTEE</div>
</div>

<footer class="site-footer">
  <div class="col c1"><h4>About Us</h4><p>TailWise – Beyond the Limits is a clean minimalistic theme that brings all the features that you are expecting from us like our other themes. It comes with a bunch of features to make your website incredible flexible so you can make every page unique if you want.</p></div>
  <div class="col c2"><h4>Affiliation</h4><div class="badges"><div class="badge-round" role="img" aria-label="Professional pet sitters association seal"></div><div class="badge-square" role="img" aria-label="Animal care and control association seal"></div></div></div>
  <div class="col c3"><h4>Say Hello!</h4><div class="input">Your Name...</div><div class="input">Your Email Address...</div><div class="input msg">Your Message...</div><div class="send">SEND YOUR MESSAGE</div></div>
  <div class="col c4"><h4>Contact Us</h4><p>482 Meadow Lane, Suite 12<br>Greenfield GV 20410<br>Phone: +1 (555) 014 2290</p><div class="social"><span></span><span></span><span></span><span></span></div></div>
</footer>
<div class="copyright">Copyright © 2016 Paw Haven. All Rights Reserved</div>

</body>
</html>
```